food company needs a design for a wafer biscuit packaging

we need a design for our wafer biscuit
There are two flavours :
first one is a chocolate wafer and its for children (the design have to be attractive to kids)
second is vanilla and its for everyone (the design must be suitable for everyone )
the design must include our logo and a file ready to go to print from the front and back
adding Arabic would be great
i've uploaded our logo and an example

```html
<!DOCTYPE html>
<html lang="en">
<head>
<meta charset="utf-8">
<title>Lunora Yummy Chocolate – Wafer Pack Front</title>
<link href="https://fonts.googleapis.com/css2?family=Fredoka:wght@500;700&family=Open+Sans:ital,wght@0,400;0,700;1,400&display=swap" rel="stylesheet">
<style>
  :root {
    --bg: #f6ecd6;
    --wrap: #a6a3d9;
    --wrap-dark: #8f8bc9;
    --orange: #f7941d;
    --orange-light: #fbb040;
    --yellow: #fcd34d;
    --cream: #f3dfa4;
    --red: #d7141f;
    --white: #ffffff;
    --choco: #5a2e17;
    --choco-light: #a0612e;
    --text-dark: #4b4678;
  }
  * { margin: 0; padding: 0; box-sizing: border-box; }
  html, body { width: 1200px; height: 747px; overflow: hidden; }
  body {
    background: var(--bg);
    font-family: "Open Sans", sans-serif;
    position: relative;
  }
  .pack {
    position: absolute;
    left: 110px; top: 170px;
    width: 980px; height: 400px;
  }
  .pack__crimp { position: absolute; top: 0; width: 60px; height: 400px; }
  .pack__crimp--left { left: 0; }
  .pack__crimp--right { right: 0; }
  .pack__body {
    position: absolute; left: 56px; right: 56px; top: 8px; bottom: 8px;
    background: var(--wrap);
    overflow: hidden;
  }
  .pack__decor { position: absolute; inset: 0; }
  .brand {
    position: absolute; left: 40px; top: 26px;
    font-family: "Fredoka", sans-serif; font-weight: 700;
    font-size: 26px; letter-spacing: 2px;
    color: var(--red);
  }
  .title {
    position: absolute; left: 95px; top: 70px;
    font-family: "Fredoka", sans-serif; font-weight: 700;
    color: var(--white); line-height: 0.9;
    transform: rotate(6deg); transform-origin: left top;
  }
  .title__small { display: block; font-size: 58px; margin-left: 40px; }
  .title__big { display: block; font-size: 74px; letter-spacing: 1px; }
  .subtitle {
    position: absolute; left: 250px; top: 226px;
    font-style: italic; font-size: 11px; color: var(--white);
    white-space: nowrap;
    transform: rotate(6deg); transform-origin: left top;
  }
  .product-shot {
    position: absolute; left: 560px; top: 50px;
    width: 270px; height: 200px;
    border-radius: 30px 30px 60px 40px;
    background: linear-gradient(160deg, var(--choco-light) 0%, var(--choco) 75%);
  }
  .tag {
    position: absolute; left: 590px; top: 222px;
    background: var(--red); color: var(--white);
    font-family: "Fredoka", sans-serif; font-weight: 700; font-size: 24px;
    padding: 8px 30px; border-radius: 40px;
    white-space: nowrap;
    transform: rotate(22deg); transform-origin: left top;
  }
  .badges {
    position: absolute; left: 40px; top: 250px;
    display: flex; gap: 16px;
  }
  .badge {
    width: 62px; height: 62px; border-radius: 50%;
    background: var(--red); color: var(--white);
    display: flex; flex-direction: column; align-items: center; justify-content: center;
    font-family: "Fredoka", sans-serif; font-weight: 700; line-height: 1;
  }
  .badge__value { font-size: 22px; }
  .badge__unit { font-size: 12px; font-weight: 500; }
  .description {
    position: absolute; left: 260px; top: 300px; width: 340px;
    font-size: 11px; line-height: 1.5; color: var(--text-dark);
  }
</style>
</head>
<body>
  <div class="pack">
    <svg class="pack__crimp pack__crimp--left" viewBox="0 0 60 400" aria-hidden="true">
      <rect x="0" y="0" width="60" height="400" fill="var(--wrap-dark)"/>
      <g stroke="var(--wrap)" stroke-width="4">
        <line x1="8" y1="0" x2="8" y2="400"/><line x1="18" y1="0" x2="18" y2="400"/>
        <line x1="28" y1="0" x2="28" y2="400"/><line x1="38" y1="0" x2="38" y2="400"/>
        <line x1="48" y1="0" x2="48" y2="400"/>
      </g>
    </svg>

    <div class="pack__body">
      <svg class="pack__decor" viewBox="0 0 868 384" preserveAspectRatio="none" aria-hidden="true">
        <path d="M60 90 C140 40 420 50 520 110 C560 140 540 200 470 215 C360 235 180 225 100 200 C40 180 20 130 60 90 Z" fill="var(--orange)"/>
        <path d="M380 60 C430 40 480 60 470 90 C440 100 400 90 380 60 Z" fill="var(--orange-light)"/>
        <path d="M0 180 C40 170 70 210 60 260 C50 310 20 330 0 330 Z" fill="var(--yellow)"/>
        <path d="M620 330 C680 290 760 300 780 384 L600 384 C600 360 605 345 620 330 Z" fill="var(--orange)"/>
        <path d="M790 200 C830 210 868 240 868 260 L868 384 L800 384 C780 320 770 250 790 200 Z" fill="var(--yellow)"/>
        <path d="M700 260 C740 250 760 300 730 330 C700 320 690 290 700 260 Z" fill="var(--cream)"/>
      </svg>

      <div class="brand">LUNORA</div>

      <h1 class="title">
        <span class="title__small">Yummy</span>
        <span class="title__big">CHOCOLATE</span>
      </h1>
      <p class="subtitle">12 wafer biscuit filled with chocolate flavored cream</p>

      <div class="product-shot" role="img" aria-label="Chocolate wafer biscuits stacked with chocolate pieces and a splash of melted chocolate"></div>
      <div class="tag">Extra Crunchie!</div>

      <div class="badges">
        <div class="badge"><span class="badge__value">35</span><span class="badge__unit">kcal</span></div>
        <div class="badge"><span class="badge__value">12</span><span class="badge__unit">units</span></div>
        <div class="badge"><span class="badge__value">NO</span><span class="badge__unit">Sodium</span></div>
      </div>

      <p class="description">Crisp wafer layers with smooth cocoa cream, baked golden and packed fresh for little hands and big smiles. Store in a cool dry place and enjoy with milk.</p>
    </div>

    <svg class="pack__crimp pack__crimp--right" viewBox="0 0 60 400" aria-hidden="true">
      <rect x="0" y="0" width="60" height="400" fill="var(--orange-light)"/>
      <g stroke="var(--yellow)" stroke-width="4">
        <line x1="12" y1="0" x2="12" y2="400"/><line x1="22" y1="0" x2="22" y2="400"/>
        <line x1="32" y1="0" x2="32" y2="400"/><line x1="42" y1="0" x2="42" y2="400"/>
        <line x1="52" y1="0" x2="52" y2="400"/>
      </g>
    </svg>
  </div>
</body>
</html>
```